"Web Design" E-commerce web site * give me the BEST Equipment website

We require an
Truely EYE catching E-COMMERCE website “Fusion Supply Australia”
Branded as FSA

**** ARE YOU UP TO THE CHALLENGE !!!! ***

We already have 2 website names registered :
www.fusegoods.com.au and www.fusionsupplyaustralia.com.au
( one is active but unfinished)

If you need to see what will APPEAL TO ME "The two websites below have a lot of what I am looking for (design Style ) www.quorvatech.com & www.zelthemes.com/live/?theme=marivanta
Therefore -a combination of these two sites best features would be very close. !
please use and index with similar catergories to: www.fusionsupplyaustralia.com.au

CONCEPT OF SITE
Customer places order through transaction system.. -all payment methods
 which immediately send order through to my own staff and or the respective supplier. (Option for site administrator to choose for each product listing who receives such email)
 Product listings must be easily edited / updated and or replaced by personell with limited computer knowledge (if they can use chatterbook or yourplace they should be able to edit product listings) simply put they will need NO CODE EDITING SKILLS REQUIRED.

Please create a pages for atleast the following:
Main home page
 Brantor products only
 Torvalk products only
 Ossari products only
 Fusequeen products only
 Electrical supplies
 Power Distribution
 Mine spec’d equipment specials
2nd hand equipment
contact
about us
sitemap

Information to populate fields with in pages can be source from our suppliers own websites as we are authorised distributors of the following sites:

http://www.brantorpower.com.au/catalogue/page3/category1
http://www.torvalk.com.au/product-category/welding-machines/
http://www.fusequeen.com.au/products/
http://www.ossari.com

concept:
Basically, the website is to be for the fast movement of stock from Our own stock and Our suppliers – direct to the customers address (drop shipping) with very LIMITED INTERACTION with our customers (email only)
Updates

           SEE IMAGES IN ATTACHED RAR    

ALSO CHECK OUT THESE SITES WHICH SHOW THE STYLES I LIKE  SO THEY WILL HELP YOU DESIGN SOMETHING THAT GETS CLOSER TO MY IDEAL SITE AND MY REQUIREMENTS

we are currently running a poll and will make a decision very shortly.. thanks to all

Target Market(s)

Males 20 to 55
engineering and handyman

Industry/Entity Type

Computer

Requirements
Must have
• That wow factor.. grabs your attention not through tacky.. but well designed / layout
Ease of editing / updating

shipping and freight calculator that automatically adds to invioce

NON compulsory Newsletter - although if customers provide validation of email they receive 2.5% discount on purchases (enter a code sent to them)

the rest is just simple.. amaze me with your talents
Nice to have
• Todays quick sales - campaign
Weekly quick sales - campaign

highlight specials

```html
<!DOCTYPE html>
<html lang="en">
<head>
<meta charset="utf-8">
<title>Fusion Supply Australia</title>
<link rel="stylesheet" href="https://fonts.googleapis.com/css2?family=Questrial&family=Open+Sans:wght@400;600;700&family=Oswald:wght@500&display=swap">
<style>
:root{
  --brown:#6b3a10;
  --brown-mid:#7a4614;
  --amber:#c87a2c;
  --amber-light:#e9a05a;
  --black:#050505;
  --white:#ffffff;
  --red:#e0201a;
  --button:#4a2a0c;
  --footer-bottom:#4b4b4b;
}
*{box-sizing:border-box;margin:0;padding:0}
html,body{width:849px;height:1200px;overflow:hidden;background:var(--black)}
body{position:relative;font-family:"Questrial",sans-serif;color:var(--white)}

.site-header{position:absolute;left:0;top:0;width:849px;height:118px;
  background:linear-gradient(180deg,#3a1a08 0%,#5a2e0e 55%,#3a1a08 100%)}
.brand{position:absolute;left:118px;top:20px;display:flex;align-items:center;gap:8px}
.brand-mark{width:14px;height:14px;background:#9a9a9a}
.brand-name{font-family:"Oswald",sans-serif;font-size:40px;line-height:40px;color:#a8a8a8;letter-spacing:2px}
.brand-sub{position:absolute;left:124px;top:61px;font-size:11px;color:var(--amber-light)}
.search{position:absolute;left:368px;top:18px;width:143px;height:19px;border:1px solid #8a6a4a;border-radius:4px;background:#2a1408;display:flex}
.search span{flex:1;font-size:8px;color:#8a7a6a;padding:4px 6px}
.search i{width:18px;background:#eee;border-radius:0 3px 3px 0}
.cart-bar{position:absolute;left:546px;top:18px;width:206px;height:21px;border-radius:4px;
  background:linear-gradient(#d98a3c,#b0621e);display:flex;font-size:8.5px;align-items:center}
.cart-bar span{padding:0 6px;border-right:1px solid #8a4a14;line-height:21px}
.cart-bar .count{width:20px;height:13px;background:#7a3e10;display:inline-block;vertical-align:middle;margin-left:4px}
.phone{position:absolute;right:97px;top:50px;font-size:8.5px;display:flex;align-items:center;gap:8px}
.phone b{font-family:"Oswald",sans-serif;font-size:16px;color:var(--amber-light);letter-spacing:1px}
.account{position:absolute;right:97px;top:74px;font-size:8px}
.account em{font-style:normal;color:var(--amber);margin:0 3px}
.main-nav{position:absolute;left:96px;top:90px;width:657px;height:28px;background:#000;border-radius:5px 5px 0 0;
  display:flex;align-items:center;gap:30px;padding-left:12px;font-size:10.5px;letter-spacing:.3px}

.content{position:absolute;left:96px;top:118px;width:657px;height:874px;
  background:linear-gradient(180deg,#4a4a4a,#2e2e2e 60%,#3a3a3a)}
.sidebar{position:absolute;left:13px;top:9px;width:133px;height:710px;background:#222}
.cat-box{position:absolute;left:5px;top:10px;width:120px;height:283px;background:var(--brown);border:1px solid #8a5a2a;border-radius:3px}
.cat-title{position:absolute;left:-4px;top:-2px;width:112px;height:30px;background:linear-gradient(#c88a3a,#8a5014);
  font-family:"Open Sans",sans-serif;font-weight:700;font-size:14px;line-height:30px;padding-left:14px;clip-path:polygon(0 0,100% 0,92% 50%,100% 100%,0 100%)}
.cat-list{position:absolute;left:5px;top:38px;width:110px;list-style:none;font-family:"Open Sans",sans-serif;font-size:9px;letter-spacing:-.1px}
.cat-list li{border-bottom:1px dashed #a07040;padding:5px 0 5px 12px;position:relative;line-height:12px;white-space:nowrap}
.cat-list li.two{white-space:normal}
.cat-list li::before{content:"";position:absolute;left:0;top:6px;width:9px;height:9px;border-radius:50%;background:#ddd}

.pay-box{position:absolute;left:5px;top:320px;width:120px;height:392px;background:var(--brown);border:1px solid #8a5a2a;border-radius:3px;
  display:grid;grid-template-columns:44px 44px;gap:14px 12px;padding:14px 0 0 10px;align-content:start}
.badge{height:28px;border-radius:2px;box-shadow:0 1px 2px rgba(0,0,0,.5)}
.badge.tall{height:50px}
.badge.wide{grid-column:span 2;width:100px;height:44px}

.slider{position:absolute;left:159px;top:11px;width:486px;height:176px;border:1px solid #777;
  background:radial-gradient(ellipse at 40% 50%,#3a3a3a,#151515 80%)}
.slide-art{position:absolute;left:14px;top:8px;width:300px;height:162px;border-radius:60px 60px 30px 30px;
  background:linear-gradient(90deg,#2a2a30 0%,#6a6a78 14%,#a07ad0 22%,#3a3a40 32%,#e0306a 42%,#40a0c0 50%,#e8a020 56%,#2a2a30 64%,#2a4aa0 72%,#c02030 84%,#1a2a6a 100%)}
.slide-text{position:absolute;left:305px;top:30px;width:170px;font-size:13px;line-height:18px;letter-spacing:.2px}
.arrow{position:absolute;top:66px;width:14px;height:22px;background:#9a9a9a}
.arrow.l{left:0}.arrow.r{right:0}
.dots{position:absolute;left:218px;top:161px;display:flex;gap:5px}
.dots i{width:8px;height:8px;border-radius:50%;background:#fff}

.section{position:absolute;left:159px;width:486px;background:var(--brown-mid);border:1px solid #a06a30}
.section-head{height:28px;display:flex;align-items:center;padding:0 14px 0 12px;font-size:15px}
.section-head svg{margin-right:4px}
.view-all{margin-left:auto;font-size:9.5px;display:flex;align-items:center;gap:3px}
.cards{display:grid;grid-template-columns:repeat(4,111px);gap:8px;padding:4px 9px 0}
.card{background:#000;border:2px solid #555;border-radius:3px;padding:4px 5px}
.card-img{height:74px}
.card-desc{font-family:"Open Sans",sans-serif;font-size:7.5px;line-height:11px;margin-top:5px;height:24px;overflow:hidden}
.card-foot{display:flex;justify-content:space-between;align-items:center;margin-top:3px}
.price{font-family:"Oswald",sans-serif;font-size:12px}
.btn{background:var(--button);border:1px solid #8a5a2a;font-family:"Open Sans",sans-serif;font-size:7.5px;padding:2px 5px}
.maker .card{height:136px;position:relative}
.maker .card-name{font-size:10.5px;line-height:12px;margin-top:6px;letter-spacing:-.2px}
.maker .btn{position:absolute;right:4px;bottom:5px;padding:2px 7px}
.maker .cards{row-gap:15px}

.testimonial{position:absolute;left:13px;top:736px;width:631px;height:127px;background:radial-gradient(ellipse at 50% 30%,#2a2a2a,#141414);border:1px solid #444}
.t-head{text-align:center;margin-top:10px;font-size:10px;color:var(--red);letter-spacing:.3px}
.t-body{position:absolute;left:46px;top:34px;width:534px;height:80px;background:#bdbdbd;border-radius:3px;color:#111;
  font-family:"Open Sans",sans-serif;font-size:7.6px;line-height:10.2px;text-align:center;padding:10px 20px}
.t-author{color:var(--red);margin-top:4px;font-size:9px}

.site-footer{position:absolute;left:0;top:992px;width:849px;height:182px;background:linear-gradient(180deg,#4a1e08,#2a1006)}
.f-col h4{font-weight:400;font-size:13px;margin-bottom:6px}
.f-col{position:absolute;top:10px}
.f-rule{position:absolute;left:108px;top:29px;width:632px;height:1px;background:#6a3a1a}
.f-links{display:flex;gap:30px;font-size:8.5px;line-height:14px}
.f-links ul{list-style:none}
.news p{font-size:8.5px;line-height:14px;width:160px;margin-top:14px}
.news-form{margin-top:22px;display:flex;width:164px;height:18px;border-radius:4px;overflow:hidden;font-size:8.5px}
.news-form span{flex:1;background:#111;padding:4px 12px}
.news-form b{font-weight:400;background:#444;padding:4px 9px}
.social{display:flex;gap:9px;margin-top:8px;justify-content:flex-end}
.social i{width:27px;height:27px;background:linear-gradient(#2a2a2a,#111);border-radius:3px}
.copyright{position:absolute;left:0;top:1174px;width:849px;height:26px;background:var(--footer-bottom);
  font-family:"Open Sans",sans-serif;font-size:7px;line-height:26px;text-align:center;color:#bbb;letter-spacing:.5px}
</style>
</head>
<body>
<header class="site-header">
  <div class="brand"><span class="brand-mark"></span><span class="brand-name">FSA</span></div>
  <div class="brand-sub">Fusion Supply Australia</div>
  <div class="search"><span>enter key words or item #</span><i></i></div>
  <div class="cart-bar"><span>Items <i class="count"></i></span><span>Total $00</span><span>View Cart</span><span style="border:0">Checkout</span></div>
  <div class="phone">Order toll-free: <b>1-800-555-0142</b></div>
  <div class="account">My Account | Sign In <em>●</em>LIVE CHAT <em>●</em>ONLINE</div>
  <nav class="main-nav"><span>HOME</span><span>ABOUT US</span><span>PRODUCTS</span><span>2ND HAND EQUIPMENT</span><span>CONTACT</span></nav>
</header>

<main class="content">
  <aside class="sidebar">
    <div class="cat-box">
      <div class="cat-title">PRODUCTS</div>
      <ul class="cat-list">
        <li>Brantor Products</li><li>Torvalk Products</li><li>Ossari Products</li><li>Fusequeen Products</li>
        <li>Electrical Supplies</li><li>Power Distribution</li><li class="two">Mine Spec'd<br>Equipment Specials</li><li>2nd Hand Equipment</li>
      </ul>
    </div>
    <div class="pay-box" role="img" aria-label="Accepted payment methods and security badges">
      <div class="badge" style="background:linear-gradient(90deg,#d0201a,#f0a020)"></div><div class="badge" style="background:linear-gradient(#fff,#e8e8e8)"></div>
      <div class="badge" style="background:linear-gradient(#fff,#e4e4e4);border:3px solid #2a4a9a"></div><div class="badge" style="background:linear-gradient(#3a7ad0,#1a5aa8)"></div>
      <div class="badge" style="background:linear-gradient(#fafafa,#d0d0d0)"></div><div class="badge" style="background:linear-gradient(#fff,#e8e8e8)"></div>
      <div class="badge tall" style="background:radial-gradient(circle,#e0c050 30%,#fff 34%)"></div><div class="badge tall" style="background:radial-gradient(circle,#e8d060,#b89020);border-radius:50%"></div>
      <div class="badge wide" style="background:linear-gradient(90deg,#c02020 0 28%,#fafafa 28%)"></div>
      <div class="badge wide" style="background:linear-gradient(#1a5a9a 0 78%,#fff 78%);height:52px"></div>
      <div class="badge wide" style="background:linear-gradient(90deg,#a8a8a8 0 30%,#e8e8e8 30%);height:46px"></div>
    </div>
  </aside>

  <section class="slider">
    <div class="slide-art" role="img" aria-label="Three decorated auto-darkening welding helmets: grey tribal, multicolour, and flag-themed"></div>
    <p class="slide-text">Lorem Ipsum. Proinrt gravida nibh vel velito iauctor aliquet. Aenea sollicitudin, lorem quii bibendum auctor, nisi consequat ipsum, nei</p>
    <span class="arrow l"></span><span class="arrow r"></span>
    <div class="dots"><i></i><i></i><i></i><i></i></div>
  </section>

  <section class="section" style="top:198px;height:181px">
    <div class="section-head">
      <svg width="30" height="18" viewBox="0 0 30 18"><path d="M2 6h4v6H2zM8 6h4v6H8zM14 5h5V0l10 9-10 9v-5h-5z" fill="#ddd"/></svg>
      New Products For July<span class="view-all">View All <svg width="6" height="9"><path d="M0 0l6 4.5L0 9z" fill="#e03a1a"/></svg></span>
    </div>
    <div class="cards">
      <div class="card"><div class="card-img" role="img" aria-label="Portable welding machine" style="background:radial-gradient(ellipse 45% 40% at 45% 50%,#2a2a2a,#e8c020 60%,#fff 100%)"></div><p class="card-desc">Lorem Ipsum proin grav sollicitudin, lorem quis</p><div class="card-foot"><span class="price">$1000</span><span class="btn">Buy Now</span></div></div>
      <div class="card"><div class="card-img" role="img" aria-label="Welding helmet" style="background:radial-gradient(ellipse 35% 45% at 50% 50%,#2a2a40,#6a6a9a 70%,#fff 100%)"></div><p class="card-desc">Lorem Ipsum proin grav sollicitudin, lorem quis</p><div class="card-foot"><span class="price">$1000</span><span class="btn">Buy Now</span></div></div>
      <div class="card"><div class="card-img" role="img" aria-label="Gas welding kit in case" style="background:radial-gradient(ellipse 48% 40% at 50% 50%,#3a6a8a,#7a9ab0 65%,#fff 100%)"></div><p class="card-desc">Lorem Ipsum proin grav sollicitudin, lorem quis</p><div class="card-foot"><span class="price">$1000</span><span class="btn">Buy Now</span></div></div>
      <div class="card"><div class="card-img" role="img" aria-label="Plasma cutter" style="background:radial-gradient(ellipse 45% 45% at 50% 50%,#3a4a6a,#8a98b0 65%,#fff 100%)"></div><p class="card-desc">Lorem Ipsum proin grav sollicitudin, lorem quis</p><div class="card-foot"><span class="price">$1000</span><span class="btn">Buy Now</span></div></div>
    </div>
  </section>

  <section class="section maker" style="top:389px;height:330px">
    <div class="section-head">
      <svg width="30" height="18" viewBox="0 0 30 18"><path d="M2 6h4v6H2zM8 6h4v6H8zM14 5h5V0l10 9-10 9v-5h-5z" fill="#ddd"/></svg>
      Products Manufacturers<span class="view-all">View All <svg width="6" height="9"><path d="M0 0l6 4.5L0 9z" fill="#e03a1a"/></svg></span>
    </div>
    <div class="cards">
      <div class="card"><div class="card-img" role="img" aria-label="Welding wire spool and box" style="background:radial-gradient(ellipse 48% 45% at 45% 50%,#8a2a1a,#c0a090 65%,#fff 100%)"></div><p class="card-name">Brantor Products</p><span class="btn">view more</span></div>
      <div class="card"><div class="card-img" role="img" aria-label="Inverter welder" style="background:radial-gradient(ellipse 42% 45% at 50% 50%,#d03a18,#e08060 65%,#fff 100%)"></div><p class="card-name">Torvalk Products</p><span class="btn">view more</span></div>
      <div class="card"><div class="card-img" role="img" aria-label="Engine driven welder" style="background:radial-gradient(ellipse 45% 45% at 50% 50%,#2a2a2a,#7a7a7a 65%,#fff 100%)"></div><p class="card-name">Ossari products</p><span class="btn">view more</span></div>
      <div class="card"><div class="card-img" role="img" aria-label="Welding gloves" style="background:radial-gradient(ellipse 40% 45% at 50% 50%,#c8ccd8,#3a4aa0 70%,#fff 100%)"></div><p class="card-name">Fusequeen Products</p><span class="btn">view more</span></div>
      <div class="card"><div class="card-img" role="img" aria-label="Track cutting machine" style="background:radial-gradient(ellipse 45% 40% at 50% 55%,#2a4aa0,#8aa0c8 65%,#fff 100%)"></div><p class="card-name">Electrical Supplies</p><span class="btn">view more</span></div>
      <div class="card"><div class="card-img" role="img" aria-label="Wire feeder unit" style="background:radial-gradient(ellipse 42% 45% at 50% 55%,#a82020,#c89080 65%,#fff 100%)"></div><p class="card-name">Power Distribution</p><span class="btn">view more</span></div>
      <div class="card"><div class="card-img" role="img" aria-label="Orange work jacket" style="background:radial-gradient(ellipse 42% 48% at 50% 50%,#d8601a,#e8a070 70%,#fff 100%)"></div><p class="card-name">Mine spec'd<br>Equipment Specials</p><span class="btn">view more</span></div>
      <div class="card"><div class="card-img" role="img" aria-label="Used inverter welder with leads" style="background:radial-gradient(ellipse 45% 45% at 45% 50%,#1a1a1a,#d06a20 45%,#9a9a9a 65%,#fff 100%)"></div><p class="card-name">2nd Hand<br>Equipment</p><span class="btn">view more</span></div>
    </div>
  </section>

  <section class="testimonial">
    <p class="t-head"><svg width="20" height="14" viewBox="0 0 20 14" style="vertical-align:middle"><ellipse cx="7" cy="6" rx="7" ry="5" fill="#2a8ad0"/><ellipse cx="13" cy="8" rx="6" ry="4.5" fill="#6ab8e8"/></svg> WHAT OUR CUSTOMERS ARE SAYING ABOUT</p>
    <div class="t-body">
      Lorem Ipsum. Proin gravida nibh vel velit auctor aliquet. Aenean sollicitudin, lorem quis bibendum auctor, nisi elit ytui kh consequat ipsum, nec sagittis sem nibh id elit. Duis sed odio sit amet nibh vulputate cursus a sit amet mauris. Morbi ua accumsan ipsum velit. Nam nec tellus a odio tincidunt auctor a ornare odio. Sed non mauris vitae erat consequat au eu in elit. Class aptent taciti sociosqu ad litora torquent per conubia nostra, per inceptos himenaeos. Mauris in erat justou.
      <p class="t-author">Darren K. &nbsp; CA</p>
    </div>
  </section>
</main>

<footer class="site-footer">
  <div class="f-rule"></div>
  <div class="f-col" style="left:108px">
    <h4>Quick link</h4>
    <div class="f-links">
      <ul><li>Home</li><li>About Us</li><li>Contact</li><li>Sitemap</li></ul>
      <ul><li>Products</li><li>- Brantor products</li><li>- Torvalk products</li><li>- Ossari products</li><li>- Fusequeen products</li><li>- Electrical supplies</li><li>- Power Distribution</li><li>- Mine spec'd equipment specials</li><li>- 2nd hand equipment</li></ul>
    </div>
  </div>
  <div style="position:absolute;left:386px;top:40px;width:1px;height:130px;background:#6a3a1a"></div>
  <div class="f-col news" style="left:401px">
    <h4>News letter</h4>
    <p>provide your validation of email to receive 2.5% discount on purchases</p>
    <div class="news-form"><span>Enter your email..</span><b>Send</b></div>
  </div>
  <div class="f-col" style="left:600px;width:140px;text-align:right">
    <h4>Be Social with US</h4>
    <div class="social" role="img" aria-label="Social network links"><i></i><i></i><i></i></div>
  </div>
</footer>
<div class="copyright">Copyright © 2013 fusionsupplyaustralia.com.au. All right reserved.</div>
</body>
</html>
```